Copperfield Roofing Co. business card design

I am a Roofing contractor in Texas. The name of my company is Copperfield Roofing Co. I also offer a few other services (Christmas light installation, gutters, fencing, pressure washing). However my main gig is roofing. Storm restoration and knowledge of the insurance claim process is my specialty.

My colors are black, red and white. I’d like something pretty simple and clean. Modern looking but with a splash of this red tartan pattern.

I have another version of my logo being edited at the moment where the little top part of the F in roofing that’s currently tartan will be changed to just solid red to make it more visible. So if that’s something you can change in your mock up great. But I can provide the full version once the contest is complete

Target Market(s)

Homeowners

Industry/Entity Type

Roofing

Contact Information for Business Card

Derek Pruitt. 682-555-0193. www.copperfield roofing.co Derek@copperfieldroofing.co

Colors
EB3D1F
EC4F4E
F09395
F8D3D4
FCEDEE

Requirements
Nice to have
• Maybe instead of a business address. I could say serving all DFW Texas or something like that. And maybe add a line somewhere saying deductible assistance? Just a thought

```html
<!DOCTYPE html>
<html lang="en">
<head>
<meta charset="utf-8">
<title>Copperfield Roofing Co. – Business Card</title>
<link href="https://fonts.googleapis.com/css2?family=Poppins:wght@400;600;700;800&display=swap" rel="stylesheet">
<style>
  :root {
    --red: #dc0b0b;
    --black: #050505;
    --white: #ffffff;
    --ink: #1a1a1a;
    --stage: #e4e4e4;
    --paper: #f7f7f7;
  }
  * { box-sizing: border-box; margin: 0; padding: 0; }
  html, body { width: 1200px; height: 930px; overflow: hidden; }
  body {
    background: var(--stage);
    font-family: "Poppins", sans-serif;
    position: relative;
  }
  .card {
    position: absolute;
    width: 640px;
    height: 366px;
    left: 280px;
    overflow: hidden;
    box-shadow: 0 6px 18px rgba(0,0,0,0.12);
  }

  /* Front: black side */
  .card--front { top: 62px; background: var(--black); }
  .brand {
    position: absolute;
    display: flex;
    align-items: center;
    gap: 16px;
  }
  .brand__dot {
    width: 78px; height: 78px;
    border-radius: 50%;
    background: var(--red);
    flex: none;
  }
  .brand__name {
    font-weight: 800;
    text-transform: uppercase;
    line-height: 1.02;
    letter-spacing: 0.02em;
  }
  .card--front .brand { left: 196px; top: 112px; }
  .card--front .brand__name { color: var(--white); font-size: 30px; }

  .band {
    position: absolute;
    left: 0; right: 0; bottom: 0;
    height: 56px;
  }
  .band__svg { position: absolute; inset: 0; }
  .band__text {
    position: absolute;
    top: 0; height: 56px;
    display: flex; align-items: center;
    color: var(--white);
    font-weight: 600;
    font-size: 17px;
  }
  .band__text--area { left: 48px; }
  .band__text--claim { left: 356px; }

  /* Back: white side */
  .card--back { top: 500px; background: var(--paper); }
  .card--back .brand { left: 150px; top: 56px; }
  .card--back .brand__name { color: var(--red); font-size: 30px; }
  .contact {
    position: absolute;
    left: 150px;
    top: 186px;
  }
  .contact__name {
    color: var(--red);
    font-weight: 600;
    font-size: 24px;
    text-transform: uppercase;
    letter-spacing: 0.02em;
    margin-bottom: 6px;
  }
  .contact__line {
    color: var(--ink);
    font-size: 17px;
    line-height: 1.45;
  }
</style>
</head>
<body>

  <section class="card card--front" aria-label="Business card front">
    <div class="brand">
      <span class="brand__dot"></span>
      <span class="brand__name">Copperfield<br>Roofing Co.</span>
    </div>
    <div class="band">
      <svg class="band__svg" width="640" height="56" viewBox="0 0 640 56" aria-hidden="true">
        <polygon points="0,0 318,0 304,56 0,56" fill="var(--red)"/>
        <polygon points="332,0 640,0 640,56 318,56" fill="var(--red)"/>
      </svg>
      <span class="band__text band__text--area">Serving all DFW Texas</span>
      <span class="band__text band__text--claim">Deductible assistance?</span>
    </div>
  </section>

  <section class="card card--back" aria-label="Business card back">
    <div class="brand">
      <span class="brand__dot"></span>
      <span class="brand__name">Copperfield<br>Roofing Co.</span>
    </div>
    <div class="contact">
      <p class="contact__name">Derek Pruitt</p>
      <p class="contact__line">682-555-0193</p>
      <p class="contact__line">Derek@copperfieldroofing.co</p>
      <p class="contact__line">www.copperfieldroofing.co</p>
    </div>
  </section>

</body>
</html>
```